Brenway Productions photography and video creator

I need a business card for my production company. I shoot photography and videography for real estate, adventure sports and businesses

simple not to busy

Colors

Designer to choose colors to be used in the design.

Requirements
Must have
• dara@brenwayproductions.ca
• phone -5803317264
• instagram dara_brenway

```html
<!DOCTYPE html>
<html lang="en">
<head>
<meta charset="UTF-8">
<title>Brenway Productions — Business Card</title>
<link href="https://fonts.googleapis.com/css2?family=Poppins:wght@400;500;600&display=swap" rel="stylesheet">
<style>
  :root {
    --backdrop: #2a2a2a;
    --card-white: #ffffff;
    --card-fade: #e6e6e6;
    --ink-dark: #3a3a3a;
    --ink-mid: #6b6b6b;
    --night: #0c0c0c;
    --ridge-light: #d4d4d4;
    --ridge-mid: #8a8a8a;
    --ridge-dark: #3b3b3b;
    --on-night: #f2f2f2;
  }
  * { margin: 0; padding: 0; box-sizing: border-box; }
  html, body {
    width: 1200px; height: 900px; overflow: hidden;
    background: var(--backdrop);
    font-family: "Poppins", sans-serif;
  }
  .canvas {
    position: relative; width: 1200px; height: 900px;
    display: flex; justify-content: center; align-items: center; gap: 60px;
  }
  .card {
    position: relative; width: 340px; height: 595px; overflow: hidden;
    box-shadow: 0 18px 40px rgba(0,0,0,0.45);
  }
  /* Front */
  .card-front {
    background: linear-gradient(160deg, var(--card-white) 35%, var(--card-fade) 100%);
    display: flex; flex-direction: column; align-items: center; justify-content: center; gap: 18px;
  }
  .brand-dot {
    width: 150px; height: 150px; border-radius: 50%;
    background: var(--ink-dark);
  }
  .brand-name {
    font-weight: 600; font-size: 22px; letter-spacing: 0.04em;
    color: var(--ink-dark); text-align: center; line-height: 1.2;
  }
  /* Back */
  .card-back { background: var(--card-white); }
  .owner {
    position: absolute; top: 34px; left: 30px;
  }
  .owner-name {
    font-weight: 500; font-size: 17px; color: var(--ink-mid); line-height: 1.2;
  }
  .owner-role {
    font-weight: 500; font-size: 10px; letter-spacing: 0.06em;
    color: var(--ink-mid); text-transform: uppercase; margin-top: 4px;
  }
  .landscape {
    position: absolute; left: 0; top: 130px; width: 340px; height: 320px;
    background: linear-gradient(180deg, var(--card-white) 0%, var(--ridge-light) 14%, var(--ridge-mid) 38%, var(--ridge-dark) 62%, var(--night) 100%);
  }
  .night-base {
    position: absolute; left: 0; top: 450px; width: 340px; height: 145px;
    background: var(--night);
  }
  .contacts {
    position: absolute; left: 30px; bottom: 34px;
    list-style: none; color: var(--on-night);
    font-size: 14px; line-height: 1.55;
  }
  .contacts li { display: flex; align-items: center; gap: 8px; }
  .contacts svg { width: 13px; height: 13px; flex: none; }
  .icon-dot {
    width: 11px; height: 11px; border-radius: 50%;
    border: 1.5px solid var(--on-night); flex: none; margin: 0 1px;
  }
</style>
</head>
<body>
<main class="canvas">
  <section class="card card-front" aria-label="Card front">
    <div class="brand-dot"></div>
    <p class="brand-name">Brenway Productions</p>
  </section>

  <section class="card card-back" aria-label="Card back">
    <header class="owner">
      <h1 class="owner-name">Dara Brenway</h1>
      <p class="owner-role">Photography and Video</p>
    </header>
    <div class="landscape" role="img" aria-label="Layered grey mountain ridges with pine trees fading into black"></div>
    <div class="night-base"></div>
    <ul class="contacts">
      <li>
        <svg viewBox="0 0 24 24" aria-hidden="true"><path fill="currentColor" d="M6.6 10.8c1.4 2.8 3.8 5.1 6.6 6.6l2.2-2.2c.3-.3.7-.4 1-.2 1.1.4 2.3.6 3.6.6.6 0 1 .4 1 1V20c0 .6-.4 1-1 1C10.6 21 3 13.4 3 4c0-.6.4-1 1-1h3.5c.6 0 1 .4 1 1 0 1.3.2 2.5.6 3.6.1.3 0 .7-.2 1L6.6 10.8z"/></svg>
        <span>580 331 7264</span>
      </li>
      <li>
        <span class="icon-dot" aria-hidden="true"></span>
        <span>dara_brenway</span>
      </li>
      <li>
        <svg viewBox="0 0 24 24" aria-hidden="true"><path fill="currentColor" d="M2 5h20v14H2V5zm2 2v.3l8 5.2 8-5.2V7H4zm16 2.7-8 5.2-8-5.2V17h16V9.7z"/></svg>
        <span>dara@brenwayproductions.ca</span>
      </li>
    </ul>
  </section>
</main>
</body>
</html>
```